Upscale sophisticated brochure for frameless shower doors, glass and related products for a glass c

We are a small family owned glass company working in the upscale area of lower Fairfield County Connectict .We are in need of a trifold brochure with a upscale / sophisticated theme. The name of our comany is Brightpane Co. Inc.
Address- 185 West Harlow Rd. , Cos Cob, Ct. 06812 phone- 203-514-7381
It should picture and have a short discription of framless shower doors. Glass table tops for bases and furniture top protection.
Mirrored walls for exersize, yoga and workout areas, bathrooms, dressing areas
Painted glass for backsplashes.pattered glass cabinet doors.
Producs and services are listed in order of importance.
The only mention of pricing is "we are competitive in our pricing".
We do have a showroom
We have been in business since 1979. That's 37 years !!
It would also need a page or area listing all other services we offer .
We are a full service glass shop. Here are some of the
services and products we offer
Shower Doors- Frameless, Sliding ,Semi Framed, Splash Panels
Shower door repair
Mirrors- clear, colored and antique for - exersize areas, gyms, bathrooms, door mirrors, dressing areas, frames,bars and backsplashes
Glass for table tops and furniture tops
Patterned glass, Painted glass, curved china cabinet glass
Saftey glass- laminated and tempered
Plexiglass
Storm and screens repaired
Fogged insulated glass replaced
Picture frame glass, window glass , plate glass
All types of glass replacement
Fireplace and wood stove glass
Showcase glass
Holes drilled for aquariums
And much more

Target Market(s)

Homeowners / (second area contractors)

Industry/Entity Type

It Company

Font styles to use
Serif

Requirements
Must have
• Photos- more traditional , some modern, brief description under /next to some photos. One page listing other services we provide
• Brief bio of who we are- family business serving Greenwich and surrouding communities since 1978.(will elaborate more when needed)
Nice to have
• Check glass company and shower door websites for ideas
• ms spray panel,
• regalclearview shower doors westport ct.
• Tovrin glass - good wording and copy
Should not have
• We do not do any commercial buildings a residential theme should be used.
• we do not do web sales
• we are not a bargain/ discount business
• do not put call now for a estimate
• pictures of product not people
• No Mailing space area. If mailed I will use a envelope.

```html
<!DOCTYPE html>
<html lang="en">
<head>
<meta charset="utf-8">
<title>Brightpane Co. Inc. – Trifold Brochure</title>
<link rel="stylesheet" href="https://fonts.googleapis.com/css2?family=Jost:wght@400;500;600&display=swap">
<style>
  :root {
    --brand-green: #1f7a12;
    --band-beige: rgba(236, 230, 214, 0.92);
    --frame-beige: #e8e1d4;
    --paper: #ffffff;
    --backdrop: #efebe4;
    --photo-gym-top: #b9bcb6;
    --photo-gym-bottom: #6b5440;
    --photo-bath-top: #d9dcdc;
    --photo-bath-bottom: #5a3b2a;
  }
  * { box-sizing: border-box; margin: 0; padding: 0; }
  html, body {
    width: 1200px; height: 1200px; overflow: hidden;
    background: var(--backdrop);
    font-family: "Jost", "Futura", sans-serif;
  }
  .brochure {
    position: absolute; left: 40px; top: 204px;
    width: 1120px; height: 792px;
    display: flex;
    box-shadow: 0 6px 18px rgba(0,0,0,0.18);
  }
  .panel { position: relative; width: 373.33px; height: 100%; background: var(--paper); overflow: hidden; }

  /* Left panel: about */
  .framed-photo {
    position: absolute; left: 41px; width: 291px; height: 190px;
    border: 7px solid var(--frame-beige);
  }
  .framed-photo.bath { top: 41px; background: linear-gradient(160deg, #e9e6de, #a9a495 60%, #cfc9bb); }
  .framed-photo.kitchen { top: 283px; background: linear-gradient(180deg, #e4e5e2 0%, #9ea39e 45%, #6e4c33 80%, #2c2621); }
  .about {
    position: absolute; left: 44px; top: 526px; width: 310px;
    color: var(--brand-green); font-size: 16px; line-height: 16.2px;
    white-space: nowrap;
  }
  .about p + p { margin-top: 16px; }

  /* Middle panel: contact */
  .hero-photo {
    position: absolute; left: 0; top: 0; width: 100%; height: 499px;
    background: linear-gradient(180deg, var(--photo-gym-top) 0%, #8d908a 40%, var(--photo-gym-bottom) 75%, #4a3a2c 100%);
  }
  .contact-block {
    position: absolute; left: 0; top: 499px; width: 100%; height: 293px;
    background: var(--brand-green); color: #fff; text-align: center;
    padding-top: 82px; font-size: 16px; line-height: 19px; letter-spacing: 0.3px;
  }
  .contact-block .company { font-weight: 600; }
  .contact-block .web { font-weight: 600; margin-top: 19px; }

  /* Right panel: cover */
  .cover-photo {
    position: absolute; left: 0; top: 0; width: 100%; height: 499px;
    background: linear-gradient(180deg, var(--photo-bath-top) 0%, #c4c6c3 55%, #a8a59c 78%, var(--photo-bath-bottom) 100%);
    border-bottom: 5px solid #4f8a3a;
  }
  .phone-band {
    position: absolute; left: 0; top: 45px; width: 100%; height: 43px;
    background: var(--band-beige);
    color: var(--brand-green); font-size: 33px; line-height: 43px;
    text-align: center; letter-spacing: 0.5px;
  }
  .tagline {
    position: absolute; left: 0; top: 570px; width: 100%;
    text-align: center; color: var(--brand-green);
    font-size: 22px; line-height: 25px;
  }
  .wordmark {
    position: absolute; left: 0; top: 668px; width: 100%;
    text-align: center; color: var(--brand-green);
    font-size: 30px; font-weight: 600; letter-spacing: 0.5px;
  }
</style>
</head>
<body>
  <div class="brochure">
    <section class="panel panel-about">
      <div class="framed-photo bath" role="img" aria-label="Photo of a traditional bathroom vanity with a framed mirror and glass shelves"></div>
      <div class="framed-photo kitchen" role="img" aria-label="Photo of a kitchen with a glass backsplash and white cabinetry"></div>
      <div class="about">
        <p>Brightpane is a family owned and<br>operated business serving Greenwich<br>and the surrounding area since 1978.<br>We are licensed, insured and<br>a member of the Shoreline Glass<br>Dealers Guild.</p>
        <p>We pride ourselves in providing quality<br>products, superior workmanship and<br>courteous, reliable service. Our staff is<br>friendly, knowledgeable and always<br>willing to provide the extra assistance<br>you may need.</p>
      </div>
    </section>

    <section class="panel panel-contact">
      <div class="hero-photo" role="img" aria-label="Photo of a home gym with a full mirrored wall and ballet barre"></div>
      <div class="contact-block">
        <div class="company">Brightpane Co. Inc.</div>
        <div>185 West Harlow Rd.</div>
        <div>Cos Cob, Connecticut 06812</div>
        <div>Phone: 203-514-7381</div>
        <div class="web">www.brightpaneinc.com</div>
      </div>
    </section>

    <section class="panel panel-cover">
      <div class="cover-photo" role="img" aria-label="Photo of a bathroom with a frameless glass shower enclosure"></div>
      <div class="phone-band">203-514-7381</div>
      <div class="tagline">Serving Greenwich<br>and Surrounding Areas<br>Since 1978</div>
      <div class="wordmark">Brightpane Co. Inc.</div>
    </section>
  </div>
</body>
</html>
```